Mexican Themed Party Invitations!

Hi,
We are wanting a Mexican themed party invititation for Dale's 40th!
We are wanting something that resembles an old Mexican postcard – like the ones you used to get in the 50’s–70's - the size would approximately be 7" by 5.5".
We would preferably like a double sided invite - The below details would be displayed on the back somewhere:
If there could also be room left somewhere on the back to attach a small magnet so that the invite can be stuck on the fridge:)
Dale's 40th
When: Saturday the 27th of July 2013 @ 7PM
Where: 48 Marlow Crescent, Coromandel Valley, SA
Bring: Yourself and cowboy drinkin’ boots
RSVP: Date, email and phone – make funny RSVP email address!
Dress: Preferably traditional Mexican or 70’s Cowboy/Girl – but tacky Sombrero’s and Ponchos are OK too!
Men: There will be a prize for the best grown (real) Mexican moustache
Music: by the Silver Cactus, Mexican Mariachi Band
Food: Supplied by……
Drinks: Bartender Trent will have the tequila shots and sangria ready to go
RSVP: by the 1st of July
Please note that we have attached some examples of pictures that we like as a bit of inspiration to give you a bit of an idea of which direction we are wanting to go in.
70's style would be good as Dale was born then.
We can't wait to see what you come up with!!!
Just for some inspration I found this image, which I love! If someone could do something like this, that would be awesome!
http://www.sales.pondvexel.com/items/r/r_mtp_lopez_card_81934.jpg
Dale's 40th insted of Juarez (or similar)

```html
<!DOCTYPE html>
<html lang="en">
<head>
<meta charset="utf-8">
<title>Party in Mexico – Dale's 40th Invitation</title>
<link rel="stylesheet" href="https://fonts.googleapis.com/css2?family=Chewy&family=Mystery+Quest&family=Nothing+You+Could+Do&family=Handlee&display=swap">
<style>
  :root {
    --frame: #1f1a26;
    --paper: #ffffff;
    --ink: #111111;
    --lime: #7ed321;
    --weave-red: #c8243a;
    --weave-brown: #6b4a2e;
    --weave-green: #2f8a4e;
    --weave-cream: #d9d2c4;
    --hat-gold: #e39b2e;
    --poncho-blue: #1e90d0;
  }
  html, body {
    margin: 0;
    padding: 0;
    width: 766px;
    height: 1200px;
    overflow: hidden;
    background: var(--paper);
  }
  .invite {
    position: relative;
    width: 766px;
    height: 1200px;
    background: var(--paper);
    color: var(--ink);
    font-family: "Nothing You Could Do", cursive;
  }
  /* Front of the postcard */
  .front {
    position: absolute;
    left: 0; top: 0;
    width: 766px; height: 600px;
    background: var(--frame);
  }
  .front__weave {
    position: absolute;
    left: 37px; top: 38px;
    width: 687px; height: 521px;
    background: linear-gradient(90deg,
      var(--weave-brown) 0%, var(--weave-cream) 12%, var(--weave-brown) 22%,
      var(--weave-red) 36%, var(--weave-brown) 48%, var(--weave-green) 60%,
      var(--weave-red) 72%, var(--weave-cream) 86%, var(--weave-red) 100%);
  }
  .front__figure {
    position: absolute;
    left: 318px; top: 118px;
    width: 370px; height: 440px;
    border-radius: 50% 50% 30% 30% / 35% 35% 20% 20%;
    background: linear-gradient(180deg, var(--hat-gold) 0%, var(--hat-gold) 40%, var(--poncho-blue) 55%, var(--poncho-blue) 100%);
  }
  .front__title {
    position: absolute;
    left: 40px; top: 170px;
    margin: 0;
    font-family: "Chewy", cursive;
    font-weight: 400;
    font-size: 64px;
    line-height: 64px;
    color: var(--lime);
    text-align: center;
    transform: rotate(-42deg);
    transform-origin: center;
    width: 360px;
  }
  /* Back of the postcard */
  .back__heading {
    position: absolute;
    left: 0; top: 637px;
    width: 766px;
    margin: 0;
    text-align: center;
    font-family: Arial, Helvetica, sans-serif;
    font-weight: 700;
    font-size: 17px;
  }
  .back__divider {
    position: absolute;
    left: 388px; top: 682px;
    width: 2px; height: 460px;
    background: var(--ink);
  }
  .back__stamp {
    position: absolute;
    left: 304px; top: 665px;
    width: 62px; height: 60px;
    border-radius: 40% 40% 30% 30%;
    background: linear-gradient(180deg, var(--hat-gold) 0%, var(--hat-gold) 45%, var(--poncho-blue) 55%, var(--poncho-blue) 100%);
  }
  .greeting {
    position: absolute;
    left: 73px; top: 668px;
    margin: 0;
    font-family: "Mystery Quest", cursive;
    font-weight: 400;
    font-size: 21px;
  }
  .headline {
    position: absolute;
    left: 32px; top: 704px;
    margin: 0;
    font-size: 24px;
    font-weight: 400;
  }
  .detail {
    position: absolute;
    margin: 0;
    font-size: 19px;
    line-height: 30px;
  }
  .detail--left { left: 32px; width: 345px; }
  .detail--right { left: 396px; width: 350px; }
  .address {
    position: absolute;
    left: 417px; top: 998px;
    margin: 0;
    font-family: "Handlee", cursive;
    font-style: normal;
    font-size: 31px;
    line-height: 41px;
  }
</style>
</head>
<body>
<main class="invite">
  <section class="front">
    <div class="front__weave" role="img" aria-label="Woven Mexican textile background with striped red, brown, green and cream patterns"></div>
    <div class="front__figure" role="img" aria-label="Cartoon figure in a golden sombrero and blue poncho with red boots"></div>
    <h1 class="front__title">Party in Mexico!</h1>
  </section>

  <section class="back">
    <h2 class="back__heading">Correo de la Fiesta</h2>
    <div class="back__divider"></div>
    <div class="back__stamp" role="img" aria-label="Small sombrero and poncho figure"></div>

    <p class="greeting">Hola, amigos!</p>
    <p class="headline">Dale's 40th is soon!</p>

    <p class="detail detail--left" style="top:757px">Saturday the 27th of July<br>Bring: yourself and your cowboy<br>drinking boots!</p>
    <p class="detail detail--left" style="top:864px">Dress: preferably traditional<br>Mexican or 70's cowboy/girl - but<br>tacky Sombrero's and Poncho's are<br>OK too!</p>
    <p class="detail detail--left" style="top:1002px">Men: There will be a prize for<br>the best grown (real) Mexican<br>moustache.</p>
    <p class="detail detail--left" style="top:1108px">Music: by the Silver Cactus,<br>Mexican Mariachi Band</p>

    <p class="detail detail--right" style="top:692px">Food supplied by ...</p>
    <p class="detail detail--right" style="top:745px">Drinks: Bartender Trent will<br>have the tequila shots and<br>sangria ready to go.</p>
    <p class="detail detail--right" style="top:860px">RSVP: by the 1st of July<br>locohombres@fiestatime.com</p>

    <address class="address">48 Marlow Crescent<br>Coromandel Valley<br>South Australia</address>
  </section>
</main>
</body>
</html>
```